Security Company Needs an UPDATED Business Card and Letterhead Design!

I run a security company and would like to have an updated BUSINESS CARD + LETTERHEAD DESIGN.

Please use my UPDATED address below:

2875 E. Thornwick Road
Suite 614 Dallas, Texas 75390

Attached is the current business card as reference, and also my logo.

Target Market(s)

High end security users such as Class A buildings, Corporate Campus Locations, Hospitals, High End Retail Centers, Warehousing, Manufacturing and High Tech Companies

Industry/Entity Type

Security Guard

Contact Information for Business Card

Looking for unique, yet professional

Requirements
Must have
• Must use the current logo and incorporate it into any design. Use the colors that are included in the logo. I also need to be able to easily add employees as the company grows. Should be an easy process to change Names and Numbers

```html
<!DOCTYPE html>
<html lang="en">
<head>
<meta charset="UTF-8">
<title>Halvern Security Group – Business Card</title>
<link rel="stylesheet" href="https://fonts.googleapis.com/css2?family=Open+Sans:wght@400;600;700&family=Roboto+Condensed:wght@700&display=swap">
<style>
  :root {
    --page-bg: #e9ebef;
    --card-bg: #ffffff;
    --navy: #1f1f6e;
    --blue: #1a6fc4;
    --blue-deep: #1d3c98;
    --blue-dark: #1a2a78;
    --text-grey: #4a4a4a;
    --text-dark: #333333;
  }
  * { margin: 0; padding: 0; box-sizing: border-box; }
  html, body {
    width: 1200px;
    height: 834px;
    overflow: hidden;
    background: var(--page-bg);
  }
  .business-card {
    position: absolute;
    left: 75px;
    top: 97px;
    width: 1050px;
    height: 640px;
    background: var(--card-bg);
    box-shadow: 0 6px 24px rgba(0, 0, 0, 0.12);
    font-family: "Open Sans", Arial, sans-serif;
  }
  .accent-band {
    position: absolute;
    left: 0;
    top: 230px;
    width: 1050px;
    height: 98px;
  }
  .company-name {
    position: absolute;
    left: 182px;
    top: 214px;
    width: 400px;
    text-align: center;
    font-family: "Open Sans", Arial, sans-serif;
    font-weight: 700;
    font-size: 32px;
    line-height: 1.3;
    color: var(--navy);
  }
  .person {
    position: absolute;
    right: 44px;
    top: 112px;
    text-align: right;
  }
  .person-name {
    font-family: "Roboto Condensed", "Arial Narrow", sans-serif;
    font-weight: 700;
    font-size: 48px;
    line-height: 1.1;
    color: var(--navy);
  }
  .person-title {
    margin-top: 6px;
    font-size: 29px;
    letter-spacing: 1.5px;
    color: var(--text-grey);
  }
  .address {
    position: absolute;
    right: 44px;
    top: 360px;
    text-align: right;
    font-style: normal;
    font-size: 29px;
    line-height: 36px;
    color: var(--text-dark);
  }
  .contact-list {
    position: absolute;
    left: 52px;
    top: 456px;
    list-style: none;
  }
  .contact-item {
    display: flex;
    align-items: center;
    height: 43px;
    font-size: 29px;
    letter-spacing: 1px;
    color: var(--text-dark);
  }
  .contact-icon {
    width: 30px;
    height: 30px;
    margin-right: 30px;
    flex: none;
  }
</style>
</head>
<body>
  <div class="business-card">
    <svg class="accent-band" viewBox="0 0 1050 98" aria-hidden="true">
      <defs>
        <linearGradient id="bandLeft" x1="0" x2="1" y1="0" y2="0">
          <stop offset="0" stop-color="var(--blue-dark)"/>
          <stop offset="1" stop-color="var(--blue)"/>
        </linearGradient>
        <linearGradient id="bandRight" x1="0" x2="1" y1="0" y2="0">
          <stop offset="0" stop-color="var(--blue)"/>
          <stop offset="1" stop-color="var(--blue-deep)"/>
        </linearGradient>
      </defs>
      <polygon points="40,0 170,0 170,98 95,98" fill="url(#bandLeft)"/>
      <polygon points="640,0 1050,0 1050,98 590,98" fill="url(#bandRight)"/>
    </svg>

    <div class="company-name">Halvern<br>Security Group</div>

    <div class="person">
      <div class="person-name">Daniel R. Whitcombe</div>
      <div class="person-title">President @ CEO</div>
    </div>

    <address class="address">
      2875 E. Thornwick Road<br>
      Suite 614<br>
      Dallas, Texas 75390
    </address>

    <ul class="contact-list">
      <li class="contact-item">
        <svg class="contact-icon" viewBox="0 0 24 24" aria-hidden="true">
          <path fill="var(--blue)" d="M3 9c0-3 4-5 9-5s9 2 9 5v2h-5V9H8v2H3z"/>
          <path fill="var(--blue)" d="M7 12h10l3 8H4z"/>
          <circle cx="12" cy="16" r="2" fill="#fff"/>
        </svg>
        602-555-0187
      </li>
      <li class="contact-item">
        <svg class="contact-icon" viewBox="0 0 24 24" aria-hidden="true">
          <rect x="2" y="5" width="20" height="14" rx="1" fill="var(--blue)"/>
          <path d="M3 6l9 7 9-7" fill="none" stroke="#fff" stroke-width="1.6"/>
        </svg>
        dan@halvernsecurity.com
      </li>
      <li class="contact-item">
        <svg class="contact-icon" viewBox="0 0 24 24" aria-hidden="true">
          <g fill="none" stroke="var(--blue)" stroke-width="1.8">
            <circle cx="12" cy="12" r="9"/>
            <ellipse cx="12" cy="12" rx="4" ry="9"/>
            <path d="M3 12h18M5 7h14M5 17h14"/>
          </g>
        </svg>
        www@halvernsecurity.com
      </li>
    </ul>
  </div>
</body>
</html>
```